serious, thorough, light and simple - that's my advice and mediations

My business card should combine my logo (uploaded file) and my homepage (https://fellor-mediation.webnestsite.com).

Contact Information for Business Card

Name: Sabine Fellor di Vanti
Phone: 076 412 58 94
mail: sfellor@postkiv.ch
web: www.fellor-di-vanti.ch

```html
<!DOCTYPE html>
<html lang="de">
<head>
<meta charset="utf-8">
<title>Wege im Dialog – Visitenkarte</title>
<link rel="stylesheet" href="https://fonts.googleapis.com/css2?family=Josefin+Sans:wght@400;600&display=swap">
<style>
  :root {
    --backdrop: #e4e4e2;
    --card-light: #ffffff;
    --card-dark: #161616;
    --gold: #a8895a;
    --green: #2f6b4c;
    --emboss: #2a2a2a;
    --shadow: rgba(0, 0, 0, 0.18);
  }
  * { box-sizing: border-box; margin: 0; padding: 0; }
  html, body {
    width: 1200px;
    height: 711px;
    overflow: hidden;
    background: var(--backdrop);
    font-family: "Josefin Sans", sans-serif;
  }
  .stage {
    position: relative;
    width: 1200px;
    height: 711px;
  }
  .card {
    position: absolute;
    top: 210px;
    width: 500px;
    height: 290px;
    border-radius: 4px;
    box-shadow: 0 10px 30px var(--shadow);
  }
  .card--front {
    left: 70px;
    background: var(--card-light);
  }
  .card--back {
    left: 630px;
    background: var(--card-dark);
  }
  .brand {
    position: absolute;
    display: flex;
    align-items: center;
    gap: 10px;
    white-space: nowrap;
  }
  .brand__dot {
    flex: none;
    border-radius: 50%;
    border-style: solid;
  }
  .brand__name {
    font-weight: 400;
    letter-spacing: 0.4px;
    line-height: 1;
  }
  .card--front .brand {
    left: 32px;
    top: 150px;
    color: var(--gold);
  }
  .card--front .brand__dot {
    width: 30px;
    height: 30px;
    border-width: 3px;
    border-color: var(--green);
  }
  .card--front .brand__name {
    font-size: 21px;
  }
  .card--back .brand {
    left: 50%;
    top: 50%;
    transform: translate(-50%, -50%);
    color: var(--emboss);
    gap: 14px;
  }
  .card--back .brand__dot {
    width: 48px;
    height: 48px;
    border-width: 2px;
    border-color: var(--emboss);
  }
  .card--back .brand__name {
    font-size: 32px;
  }
  .contact {
    position: absolute;
    left: 282px;
    top: 84px;
    color: var(--gold);
    white-space: nowrap;
  }
  .contact__name {
    font-size: 14px;
    font-weight: 400;
    letter-spacing: 0.6px;
    text-transform: uppercase;
    margin-bottom: 16px;
  }
  .contact__list {
    list-style: none;
    font-size: 12px;
    line-height: 1;
  }
  .contact__item {
    display: flex;
    align-items: center;
    gap: 8px;
    margin-bottom: 9px;
  }
  .contact__icon {
    width: 11px;
    height: 11px;
    fill: var(--green);
    flex: none;
  }
</style>
</head>
<body>
<main class="stage">
  <section class="card card--front" aria-label="Vorderseite">
    <div class="brand">
      <span class="brand__dot"></span>
      <span class="brand__name">Wege im Dialog</span>
    </div>
    <div class="contact">
      <p class="contact__name">Sabine Fellor di Vanti</p>
      <ul class="contact__list">
        <li class="contact__item">
          <svg class="contact__icon" viewBox="0 0 24 24" aria-hidden="true"><path d="M6.6 10.8a15 15 0 0 0 6.6 6.6l2.2-2.2a1 1 0 0 1 1-.25 11.4 11.4 0 0 0 3.6.57 1 1 0 0 1 1 1V20a1 1 0 0 1-1 1A17 17 0 0 1 3 4a1 1 0 0 1 1-1h3.5a1 1 0 0 1 1 1c0 1.25.2 2.45.57 3.57a1 1 0 0 1-.25 1z"/></svg>
          <span>076 412 58 94</span>
        </li>
        <li class="contact__item">
          <svg class="contact__icon" viewBox="0 0 24 24" aria-hidden="true"><path d="M2 5h20v14H2z M4 7v.5l8 5 8-5V7l-8 5z" fill-rule="evenodd"/></svg>
          <span>sfellor@postkiv.ch</span>
        </li>
        <li class="contact__item">
          <svg class="contact__icon" viewBox="0 0 24 24" aria-hidden="true"><path d="M12 2a10 10 0 1 0 0 20 10 10 0 0 0 0-20zm6.9 6h-3a15 15 0 0 0-1.3-3.9A8 8 0 0 1 18.9 8zM12 4c.8 1.2 1.5 2.5 1.9 4h-3.8c.4-1.5 1.1-2.8 1.9-4zM4.3 14a8 8 0 0 1 0-4h3.4a16 16 0 0 0 0 4zm.8 2h3a15 15 0 0 0 1.3 3.9A8 8 0 0 1 5.1 16zm3-8h-3a8 8 0 0 1 4.3-3.9C8.8 5.3 8.4 6.6 8.1 8zM12 20c-.8-1.2-1.5-2.5-1.9-4h3.8c-.4 1.5-1.1 2.8-1.9 4zm2.3-6H9.7a14 14 0 0 1 0-4h4.6a14 14 0 0 1 0 4zm.3 5.9c.6-1.2 1-2.5 1.3-3.9h3a8 8 0 0 1-4.3 3.9zm1.7-5.9a16 16 0 0 0 0-4h3.4a8 8 0 0 1 0 4z"/></svg>
          <span>www.fellor-di-vanti.ch</span>
        </li>
      </ul>
    </div>
  </section>

  <section class="card card--back" aria-label="Rückseite">
    <div class="brand">
      <span class="brand__dot"></span>
      <span class="brand__name">Wege im Dialog</span>
    </div>
  </section>
</main>
</body>
</html>
```